Pricing and Packages Page

#1 Just looking for a design no coding
We Are looking for a Design of the PRICING AND PACKAGES page. The home page is just for reference material.
Winner will be contacted and possibly hired to do additional jobs.
Brightvale Real Estate needs a web page design for our bundles. We need it to be visually appeal and an emphasis placed on the premium bundle. Attached are some pngs of our current page, and a paint mock up of an idea of our layout. Please try and stay within the theme of the top menu bars of the paint file. Whites, Blues, Oranges, and Light Grays would be preferred.
Provided is a mock-up of our home screen. We want easy to read yet an initiative for people to select home listing packages on our website. Possible reference websites would be havenlot.example and plotsellhub.example or any website that has packages and pricing to choose from.
The top of the page should include the title Packages & Pricing.
Below that we want to have it easily read and illustrated that the will "Pay Nothing Until Home Sold"
Next to that a space to enter a anticipated sales price, asking the question, how much will you save. Much sure this is emphasized.
Include the bundles, which are separated into three packages, Basic, Premium and Multi-List Package. Please include the Bundle Prices of $179, $249 and $499 along with + Transaction Coordination Fee $299. Have a spot for a Get Started Button.
The boxes on the side are just an example of what to include with the prices.
Transaction Coordination Fee and All Listings Include, We just want the text display in a way where the page isnt text heavy but illustrated.
Additional Services Offered, Just a basic list with prices next to it.
Paint

```html
<!DOCTYPE html>
<html lang="en">
<head>
<meta charset="utf-8">
<title>Packages &amp; Pricing – Brightvale Real Estate</title>
<link href="https://fonts.googleapis.com/css2?family=Open+Sans:wght@400;600;700;800&display=swap" rel="stylesheet">
<style>
:root{
  --navy:#14478f;
  --blue:#1b5fb0;
  --sky:#2aa7ea;
  --deep:#0b3f86;
  --orange:#f58220;
  --orange-dark:#e06a0c;
  --ink:#2b2b2b;
  --muted:#666;
  --grey:#eeeeee;
  --grey-2:#dcdcdc;
  --white:#fff;
  --black:#1d1d1d;
}
*{box-sizing:border-box;margin:0;padding:0}
html,body{width:1200px;height:2400px;overflow:hidden}
body{position:relative;font-family:"Open Sans",Arial,sans-serif;color:var(--ink);background:var(--white);font-size:13px}
.abs{position:absolute}

/* top bar */
.topbar{left:0;top:0;width:1200px;height:28px;background:var(--navy);color:var(--white);font-size:11px;font-weight:600}
.topbar .nav{left:120px;top:0;display:flex;gap:34px;line-height:28px;letter-spacing:.3px}
.topbar .phone{left:816px;line-height:28px;font-weight:700;font-size:12px}
.topbar .help{left:907px;top:0;width:173px;height:28px;background:var(--orange);text-align:center;line-height:28px;font-size:10px}

/* header */
.header{left:0;top:28px;width:1200px;height:70px;border-bottom:1px solid #e3e3e3}
.brand{left:120px;top:22px;display:flex;align-items:center;gap:8px;font-size:24px;font-weight:700;color:var(--blue)}
.brand .mark{width:26px;height:26px;background:var(--orange)}
.user{left:930px;top:16px;width:150px;height:38px;border-radius:19px;background:#f1f1f1;display:flex;align-items:center;gap:10px;padding-left:4px;font-size:11px;font-weight:700}
.user .avatar{width:30px;height:30px;border-radius:50%;background:linear-gradient(#b9a089,#7d6452)}
.user .caret{margin-left:auto;margin-right:12px;border:5px solid transparent;border-top-color:#666;margin-top:5px}

/* estimator */
.estimator{left:120px;top:137px;width:960px;height:177px;border:7px solid var(--orange);display:flex}
.estimator .lead{width:300px;background:var(--grey);text-align:center;padding-top:28px}
.lead h1{font-size:22px;font-weight:600;color:#333}
.lead .zero{display:flex;justify-content:center;align-items:center;gap:10px;margin-top:8px}
.lead .zero b{font-size:52px;font-weight:800;color:var(--navy);line-height:1}
.lead .zero span{text-align:left;font-size:15px;line-height:1.25;color:#333}
.estimator .calc{padding:28px 0 0 40px}
.calc h2{font-size:24px;font-weight:700;color:var(--ink)}
.calc .ask{margin-top:6px;font-size:11px;font-weight:700;color:var(--blue)}
.calc .fields{display:flex;gap:14px;margin-top:8px}
.calc .field{width:250px;height:30px;border:1px solid #ccc;font-size:10px;color:#999;padding:8px 10px}
.calc .go{width:78px;height:30px;background:var(--orange);color:var(--white);font-weight:700;text-align:center;line-height:30px;font-size:13px}
.calc .hint{margin-top:10px;font-size:11px}

/* pricing */
.pricing{left:0;top:348px;width:1200px;height:773px;background:radial-gradient(ellipse 600px 420px at 560px 320px,#42c6f5 0%,#1f95e0 45%,var(--deep) 100%)}
.most{left:0;width:1200px;top:40px;text-align:center;color:var(--white);font-size:22px;font-weight:800;padding-left:240px}
.features{left:144px;top:230px;width:272px;height:392px;background:linear-gradient(90deg,rgba(255,255,255,.96),rgba(255,255,255,.82))}
.features li,.plan li{list-style:none;border-bottom:1px solid #d2d2d2;display:flex;align-items:center;font-size:12px}
.features li{padding-left:30px;color:#333;line-height:1.35}
.note{left:170px;top:629px;color:var(--white);font-size:10.5px;font-weight:600}
.r1{height:39px}.r2{height:48px}.r3{height:36px}.r4{height:45px}.r5{height:111px}.r6{height:50px}.r7{height:58px}
.plan{background:linear-gradient(#f5f5f5,#dedede);box-shadow:0 6px 18px rgba(0,0,0,.35)}
.plan .name{background:var(--black);color:var(--white);text-align:center;font-size:15px}
.plan .price{background:linear-gradient(#3a3a3a,#111);color:var(--white);text-align:center}
.plan .price b{font-size:66px;font-weight:400;line-height:1}
.plan .price sup{font-size:28px;vertical-align:top;position:relative;top:8px}
.plan .price small{display:block;font-size:9px;margin-top:4px}
.plan li{justify-content:center}
.plan .cta{margin:22px auto 0;width:172px;height:28px;background:#1e1e1e;border-radius:3px;color:var(--white);font-size:13px;line-height:28px;padding-left:14px;position:relative}
.plan .cta::after{content:"";position:absolute;right:8px;top:6px;width:28px;height:16px;background:var(--orange);clip-path:polygon(0 0,35% 0,60% 50%,35% 100%,0 100%,25% 50%,40% 0,75% 0,100% 50%,75% 100%,40% 100%,65% 50%)}
.basic{left:413px;top:103px;width:206px;height:586px}
.basic .name,.mls .name{height:22px;line-height:22px}
.basic .price,.mls .price{height:93px;padding-top:12px}
.premium{left:624px;top:91px;width:211px;height:617px;background:linear-gradient(#fff,#e6e6e6);z-index:2}
.premium .name{height:24px;line-height:24px;background:#2a2a2a}
.premium .price{height:115px;padding-top:22px;background:linear-gradient(#ffb23a,var(--orange-dark))}
.mls{left:840px;top:103px;width:202px;height:586px}

/* transaction */
.section-title{width:1200px;left:0;text-align:center;font-size:21px;font-weight:800;color:var(--black)}
.subtitle{width:1200px;left:0;text-align:center;color:var(--blue);font-size:14px;font-weight:600}
.para{width:1200px;left:0;text-align:center;font-size:12.5px;color:#333}
.pill{left:516px;top:1265px;width:168px;height:33px;border-radius:17px;background:var(--navy);color:var(--white);font-weight:700;font-size:12px;text-align:center;line-height:33px}
.perk{width:300px;text-align:center;font-size:11.5px;color:#333;line-height:1.4}
.perk svg{display:block;margin:0 auto 22px;width:54px;height:54px}

/* services */
.services-bg{left:0;top:1656px;width:1200px;height:528px;background:#f2f2f2}
.services{left:302px;top:1819px;width:591px;height:257px;background:var(--white);box-shadow:0 0 0 8px #fafafa,0 1px 6px rgba(0,0,0,.12)}
.services .head{height:43px;background:var(--navy);color:var(--white);display:flex;font-weight:700;font-size:14px;align-items:center}
.services .row{display:flex;align-items:center;height:53.5px;border-bottom:1px solid #e2e2e2;font-size:12px}
.services .row:nth-child(3){background:#f3f3f3}
.c1{width:277px;padding-left:42px}.c2{width:158px;padding-left:20px;color:#777}.c3{flex:1;text-align:center;color:#777;border-left:1px solid #e2e2e2;height:100%;line-height:53px}
.head .c1,.head .c2{color:var(--white)}
.checkbox{display:inline-block;width:16px;height:16px;border:1px solid #aaa;background:var(--white);vertical-align:middle;margin-left:8px}

/* footer */
.skyline{left:0;top:2112px;width:1200px;height:72px;background:linear-gradient(transparent 0%,#8ab0d8 40%,var(--navy) 100%)}
.footer{left:0;top:2184px;width:1200px;height:175px;background:var(--navy);color:var(--white);font-size:11px}
.footer ul{position:absolute;top:32px;list-style:none;width:150px}
.footer li{height:21px;border-bottom:1px solid rgba(255,255,255,.25);line-height:20px}
.news{left:780px;top:30px;width:300px}
.news .in{margin-top:8px;display:flex}
.news .in span{width:264px;height:34px;background:var(--white)}
.news .in b{width:36px;height:34px;background:var(--orange);display:flex;align-items:center;justify-content:center}
.social{display:flex;gap:6px;margin-top:24px}
.social span{width:26px;height:26px;background:#2d68b5}
.bottom{left:0;top:2359px;width:1200px;height:41px;background:var(--deep);color:#b9cbe6;font-size:10px}
.bottom .l{left:120px;line-height:41px}.bottom .r{right:120px;line-height:41px}
</style>
</head>
<body>

<div class="topbar abs">
  <div class="nav abs"><span>SEARCH LISTINGS</span><span>WHY CHOOSE BRIGHTVALE</span><span>DIRECTORY</span><span>GUIDES</span></div>
  <div class="phone abs">+ 000-555-0147</div>
  <div class="help abs">FAQ'S / CONTACT US / HELP</div>
</div>

<header class="header abs">
  <div class="brand abs"><span class="mark"></span>BrightvaleRealEstate</div>
  <div class="user abs"><span class="avatar" role="img" aria-label="user profile photo"></span>JORDAN M.<span class="caret"></span></div>
</header>

<section class="estimator abs">
  <div class="lead">
    <h1>Packages &amp; Pricing</h1>
    <div class="zero"><b>$0</b><span>Pay Nothing<br>Until Home Sold</span></div>
  </div>
  <div class="calc">
    <h2>Maximum Market Exsposure Guaranteed!</h2>
    <div class="ask">HOW MUCH WILL YOU SAVE?</div>
    <div class="fields"><div class="field">$</div><div class="field">My listing</div><div class="go">SEARCH</div></div>
    <div class="hint">Enter Estimated Sales Price</div>
  </div>
</section>

<section class="pricing abs">
  <div class="most abs">MOST POPULAR!</div>
  <ul class="features abs">
    <li class="r1">Listing on brightvale.example</li>
    <li class="r2">Earn Featured Listing on<br>brightvale.example</li>
    <li class="r3">Photos</li>
    <li class="r4">Free Brokers Price Opinion</li>
    <li class="r5">Exposure on over 50+<br>real estate Websites<br>including:<br>Homespire<br>Nestory<br>Roofline Homes</li>
    <li class="r6">Premium Yard Sign<br>With Mobil ID#</li>
    <li class="r7">Listing on Local<br>MLS*</li>
  </ul>
  <div class="note abs">This Requires a 3% Buyers Agent Commission.</div>

  <div class="plan basic abs">
    <div class="name">Basic</div>
    <div class="price"><b><sup>$</sup>199</b><small>+ Transaction Coordination Fee $299.</small></div>
    <ul><li class="r1">x</li><li class="r2">x</li><li class="r3">6</li><li class="r4"></li><li class="r5"></li><li class="r6"></li><li class="r7"></li></ul>
    <div class="cta">Get Started</div>
  </div>
  <div class="plan premium abs">
    <div class="name">Premium</div>
    <div class="price"><b><sup>$</sup>249</b><small>+ Transaction Coordination Fee $299.</small></div>
    <ul><li class="r1">x</li><li class="r2">x</li><li class="r3">Unlimited</li><li class="r4">x</li><li class="r5">x</li><li class="r6">x</li><li class="r7"></li></ul>
    <div class="cta">Get Started</div>
  </div>
  <div class="plan mls abs">
    <div class="name">MLS</div>
    <div class="price"><b><sup>$</sup>499</b><small>+ Transaction Coordination Fee $299.</small></div>
    <ul><li class="r1">x</li><li class="r2">x</li><li class="r3">Unlimited</li><li class="r4">x</li><li class="r5">x</li><li class="r6">x</li><li class="r7">x</li></ul>
    <div class="cta">Get Started</div>
  </div>
</section>

<h2 class="section-title abs" style="top:1166px">TRANSACTION COORDINATION FEE</h2>
<div class="subtitle abs" style="top:1202px">No Worries</div>
<p class="para abs" style="top:1226px">As the transaction coordinator, Brightvale Real Estate will guid the buyer and seller through the entire transaction in an efficient and worry free way.</p>
<div class="pill abs">ALL LISTINGS INCLUDE</div>

<div class="perk abs" style="left:102px;top:1350px">
  <svg viewBox="0 0 54 54"><circle cx="24" cy="24" r="18" fill="none" stroke="#f58220" stroke-width="6"/><path d="M14 25l8 8 18-20" fill="none" stroke="#f58220" stroke-width="6" stroke-linecap="round"/><rect x="6" y="46" width="40" height="6" fill="#f58220"/></svg>
  Only Pre - Approved Buyers</div>
<div class="perk abs" style="left:450px;top:1350px">
  <svg viewBox="0 0 54 54"><circle cx="27" cy="30" r="22" fill="#f58220"/><path d="M13 32l14-13 14 13v11H13z" fill="#fff"/><rect x="23" y="34" width="8" height="9" fill="#f58220"/></svg>
  Schedule Open Houses</div>
<div class="perk abs" style="left:769px;top:1350px">
  <svg viewBox="0 0 54 54"><path d="M8 46L40 14" stroke="#f58220" stroke-width="7" stroke-linecap="round"/><circle cx="42" cy="12" r="8" fill="none" stroke="#f58220" stroke-width="5"/><path d="M10 10l36 36" stroke="#f58220" stroke-width="6" stroke-linecap="round"/></svg>
  Step by Step Guides &amp; Tools</div>
<div class="perk abs" style="left:102px;top:1500px">
  <svg viewBox="0 0 54 54"><circle cx="27" cy="27" r="22" fill="none" stroke="#f58220" stroke-width="10"/><circle cx="27" cy="27" r="22" fill="none" stroke="#fff" stroke-width="10" stroke-dasharray="9 25.5"/></svg>
  Customer Support 7 Days a Week via<br>Email, Phone &amp; Chat</div>
<div class="perk abs" style="left:450px;top:1500px">
  <svg viewBox="0 0 54 54"><path d="M4 22l12-8 12 8-12 10z" fill="#f58220"/><path d="M50 22l-12-8-12 8 12 10z" fill="#f58220"/><rect x="16" y="24" width="22" height="12" rx="5" fill="#f58220"/></svg>
  Contract Negotion Support</div>
<div class="perk abs" style="left:769px;top:1500px">
  <svg viewBox="0 0 54 54"><path d="M18 12a12 12 0 0 1 18 0M13 7a19 19 0 0 1 28 0" fill="none" stroke="#f58220" stroke-width="3"/><rect x="19" y="18" width="16" height="24" rx="3" fill="#f58220"/><rect x="25" y="42" width="4" height="10" fill="#f58220"/></svg>
  Listing Stat Tracking</div>

<div class="services-bg abs"></div>
<h2 class="section-title abs" style="top:1696px">ADDITIONAL SERVICES OFFERED</h2>
<p class="para abs" style="top:1734px;font-size:11.5px">Payment Due When Service is Completed</p>
<div class="subtitle abs" style="top:1760px;font-size:13px">Will yoe offer a 3% buyers agent commission?<span class="checkbox"></span></div>
<div class="services abs">
  <div class="head"><span class="c1">Services</span><span class="c2">Price</span></div>
  <div class="row"><span class="c1">Professional<br>Photography</span><span class="c2">$ xxx</span><span class="c3">Add</span></div>
  <div class="row"><span class="c1">Professional House<br>Staging</span><span class="c2">$ xxx</span><span class="c3">Add</span></div>
  <div class="row"><span class="c1">Broker Price Opinion</span><span class="c2">$ xxx</span><span class="c3">Add</span></div>
  <div class="row"><span class="c1">Premium Yard Signs</span><span class="c2">$ xxx</span><span class="c3">Add</span></div>
</div>

<div class="skyline abs" role="img" aria-label="city skyline silhouette in blue"></div>
<footer class="footer abs">
  <ul style="left:120px"><li>About</li><li>Research</li><li>Services</li><li>Contact Us</li><li>Why Choose Us</li></ul>
  <ul style="left:331px"><li>Search Listings</li><li>Real Estate Guides</li><li>Neighborhood Info</li><li>Get Pre-Approved</li><li>Fair Housing Laws &amp; Information</li></ul>
  <ul style="left:540px"><li>Disclaimers</li><li>Feedback</li><li>Terms &amp; Conditions</li><li>Help</li></ul>
  <div class="news abs">Enter your email adress to sign for our newsletter
    <div class="in"><span></span><b><svg width="16" height="14" viewBox="0 0 16 14"><path d="M1 7h12M8 2l5 5-5 5" fill="none" stroke="#fff" stroke-width="2.4"/></svg></b></div>
    <div class="social"><span></span><span></span><span></span><span></span><span></span></div>
  </div>
</footer>
<div class="bottom abs"><span class="l abs">© 2014 Brightvale Real Estate | All rights reserved</span><span class="r abs">Powered by Larkfield Web Works Ltd</span></div>

</body>
</html>
```